Boilerplate Management Organization Chart

"Our Management Approach is a deliberate step-by-step process and supports our Technical Approach detailed in proposal submission. The Management Approach covers all the human capital aspects for executing a contract—from contract award through to sustainment and/or transition of the contract to another company. It includes how we organize, hire, staff, train, and account for our contract employees—as well as their complete personal life-cycle management within the company."

We need this management approach to depict an amazing management process that demonstrates best practices of the project management body of knowledge. We need this vector image to be applicable to any proposal without making references to any other proposals. Generic names but using strong business language.
Updates

Thanks for all designs submitted thus far. Some have stuck to the original type of chart. We would like to see a completely different way to show the same information. It has to be able to be recognized and deciphered very quickly by people who might not necessarily want to look at it. It must draw them in and make it incredibly easy to distinguish a management approach that looks fresh, infallible, and easily implemented.

Target Market(s)

Federal space, Government organizations looking for procedural efficiencies,

Industry/Entity Type

Management

Requirements
Must have
• Must not take up more than 1/3 to 1/2 of printable page and be clear.
Should not have
• Not too much color, but should stick to some color palette of some interest.

```html
<!DOCTYPE html>
<html lang="en">
<head>
<meta charset="utf-8">
<title>Management Approach</title>
<link rel="stylesheet" href="https://fonts.googleapis.com/css2?family=Exo+2:ital,wght@1,800&family=Poppins:wght@800&family=Rubik:wght@700&display=swap">
<style>
  :root {
    --page: #ffffff;
    --panel: #d6d2c5;
    --teal: #13b1a8;
    --orange: #f7820f;
    --label: #5f6170;
    --white: #ffffff;
  }
  html, body {
    margin: 0;
    padding: 0;
    width: 1200px;
    height: 1200px;
    overflow: hidden;
    background: var(--page);
  }
  .chart { display: block; width: 1200px; height: 1200px; }
  .panel { fill: var(--panel); }
  .title {
    font-family: "Exo 2", sans-serif;
    font-style: italic;
    font-weight: 800;
    font-size: 50px;
    letter-spacing: 9px;
    fill: var(--orange);
  }
  .title-rule, .flow-path, .program-bracket {
    fill: none;
    stroke: var(--orange);
    stroke-width: 3;
    stroke-dasharray: 2 6;
    stroke-linecap: round;
  }
  .step-box { fill: var(--teal); }
  .step-number {
    font-family: "Poppins", sans-serif;
    font-weight: 800;
    font-size: 62px;
    fill: var(--white);
    text-anchor: middle;
  }
  .connector {
    fill: none;
    stroke: var(--teal);
    stroke-width: 3;
  }
  .node { fill: var(--orange); }
  .step-label {
    font-family: "Rubik", sans-serif;
    font-weight: 700;
    font-size: 25px;
    fill: var(--label);
  }
  .step-label.right { text-anchor: end; }
  .program-label {
    font-family: "Rubik", sans-serif;
    font-weight: 700;
    font-size: 38px;
    fill: var(--orange);
    text-anchor: middle;
  }
</style>
</head>
<body>
<svg class="chart" viewBox="0 0 1500 1500" xmlns="http://www.w3.org/2000/svg" aria-label="Management approach process">
  <rect class="panel" x="175" y="83" width="1150" height="1334"/>

  <!-- heading -->
  <text class="title" x="265" y="180">MANAGEMENT</text>
  <line class="title-rule" x1="270" y1="192" x2="660" y2="192"/>
  <text class="title" x="275" y="242">APPROACH</text>

  <!-- process flow -->
  <polyline class="flow-path" points="691,358 836,480 691,594 836,715 691,834 836,967 691,1083 836,1204"/>

  <!-- left column steps -->
  <g class="step step-left">
    <path class="connector" d="M475 359 H691 M392 418 V508"/>
    <rect class="step-box" x="336" y="300" width="139" height="118" rx="2"/>
    <text class="step-number" x="402" y="381">01</text>
    <text class="step-label" x="410" y="474">RESPONSIBILITY FIXED</text>
  </g>
  <g class="step step-left">
    <path class="connector" d="M475 594 H691 M392 656 V746"/>
    <rect class="step-box" x="336" y="538" width="139" height="118" rx="2"/>
    <text class="step-number" x="404" y="619">03</text>
    <text class="step-label" x="430" y="712">MANNING THE TEAM</text>
  </g>
  <g class="step step-left">
    <path class="connector" d="M475 834 H691 M392 893 V985"/>
    <rect class="step-box" x="336" y="775" width="139" height="118" rx="2"/>
    <text class="step-number" x="406" y="856">05</text>
    <text class="step-label" x="430" y="933">PROFESSION</text>
    <text class="step-label" x="430" y="966">DEVELOPMENT</text>
  </g>
  <g class="step step-left">
    <path class="connector" d="M475 1083 H691 M392 1142 V1233"/>
    <rect class="step-box" x="336" y="1024" width="139" height="118" rx="2"/>
    <text class="step-number" x="404" y="1104">07</text>
    <text class="step-label" x="441" y="1197">BENEFITS</text>
  </g>

  <!-- right column steps -->
  <g class="step step-right">
    <path class="connector" d="M836 481 H1054 M962 329 H1144 V419"/>
    <rect class="step-box" x="1054" y="419" width="139" height="118" rx="2"/>
    <text class="step-number" x="1120" y="499">02</text>
    <text class="step-label right" x="1128" y="373">MANAGEMENT &amp; OVERSIGHT</text>
  </g>
  <g class="step step-right">
    <path class="connector" d="M836 716 H1052 M962 570 H1144 V657"/>
    <rect class="step-box" x="1052" y="657" width="139" height="118" rx="2"/>
    <text class="step-number" x="1122" y="738">04</text>
    <text class="step-label right" x="1128" y="610">TRAINING</text>
  </g>
  <g class="step step-right">
    <path class="connector" d="M836 967 H1052 M962 814 H1144 V905"/>
    <rect class="step-box" x="1052" y="905" width="139" height="118" rx="2"/>
    <text class="step-number" x="1123" y="988">06</text>
    <text class="step-label right" x="1118" y="848">RETENTION /</text>
    <text class="step-label right" x="1118" y="880">QUALITY OF LIFE</text>
  </g>
  <g class="step step-right">
    <path class="connector" d="M836 1205 H1054 M962 1056 H1144 V1143"/>
    <rect class="step-box" x="1054" y="1143" width="139" height="118" rx="2"/>
    <text class="step-number" x="1126" y="1218">08</text>
    <text class="step-label right" x="1120" y="1090">SUSTAINMENT /</text>
    <text class="step-label right" x="1120" y="1122">TRANSITION</text>
  </g>

  <!-- flow nodes -->
  <g class="nodes">
    <circle class="node" cx="691" cy="358" r="11"/>
    <circle class="node" cx="836" cy="480" r="11"/>
    <circle class="node" cx="691" cy="594" r="11"/>
    <circle class="node" cx="836" cy="715" r="11"/>
    <circle class="node" cx="691" cy="834" r="11"/>
    <circle class="node" cx="836" cy="967" r="11"/>
    <circle class="node" cx="691" cy="1083" r="11"/>
    <circle class="node" cx="836" cy="1204" r="11"/>
  </g>

  <!-- program development bracket -->
  <polyline class="program-bracket" points="235,1245 235,1357 462,1357"/>
  <polyline class="program-bracket" points="1038,1357 1268,1357 1268,1240"/>
  <text class="program-label" x="750" y="1370">PROGRAM DEVELOPMENT</text>
</svg>
</body>
</html>
```